Creative, Modern and Conversion based Web Design

Kovel Digital has recently launched a new logo and as part of our companies rebranding, we need a new website aimed towards the UK B2B marketplace.

The website needs to deliver a modern and creative website design whilst ensuring the design is tailored towards conversion optimisation.

This site must drive point of contact either from an online form, via a direct telephone call or Skype connection.

Our sales are all offline so the website will be a simple, elegant and stunning information portal.

Kovel Digital offers Digital Marketing services to companies throughout the UK - our target audiences are companies that turnover a minimum of 3 million pounds a year and as such we need to deliver a professional image that installs confidence in our companies abilities.

We do not like websites that are reliant upon stock photography - we are happy for stock photography to be used in a small way however the site must not look like a template filled with stock photography.

What do we do

We supply digital marketing services to those companies who demand a strong return on investment - our company prides itself on delivering successful campaigns that help establish long-term profitable relationships.

A lot of the information presented on our old site is relevant today however the design sucks. So please use the information on our current website as a foundation for your design content.

I am looking for several page designs including

"Home Page" Desktop Version
"Service Page" Desktop Version
"Blog Page" Desktop Version

"Home Page" Mobile Version
"Service Page" Mobile Version
"Blog Page" Mobile Version

In the 1st instance please only submit a single design for the "Home Page" Desktop Version - those designers that we are impressed with will be asked to complete the other designs before a winner is selected.

I like modern clean fonts - the site needs to welcome the reader and encourage them to absorb the information - not to overload and make them leave.

The site must be designed to naturally fit our companies new logo.

NO TEMPLATES

Target Market(s)

B2b - 3 million turnover and above

Industry/Entity Type

Digital Marketing

Number of Pages Required

3 page

Requirements
Must have
• Blended well with the companies logo
• We need conversion optimisation to be a huge part of the design - we considered a conversation when a potential customer reaches out to use via - web form, telephone or skype
• The current content on the old website fits today's business but the design sucks.
• www.koveldigital-studio.net
Nice to have
• We need 3 pages (in 2 variants Desktop and Mobile)
• Home Page
• Service Page
• Blog Page
• Please only deliver the "Home Page" desktop version - if we are happy with your design we will aks for the additional pages
Should not have
• No templates and not stock photo heavy design

```html
<!DOCTYPE html>
<html lang="en">
<head>
<meta charset="utf-8">
<title>Kovel Digital – Digital Marketing</title>
<link href="https://fonts.googleapis.com/css2?family=Roboto:ital,wght@0,300;0,400;0,500;0,700;0,900;1,400;1,500&display=swap" rel="stylesheet">
<style>
:root{
  --blue:#163e9e;
  --blue-dark:#0f2f86;
  --navy:#0a1f5c;
  --ink:#1d1d1d;
  --muted:#8b8b8b;
  --line:#d6d6d6;
  --ghost:#ececec;
  --grey-card:#6c6c6c;
  --footer:#2b2b2b;
  --white:#ffffff;
}
*{margin:0;padding:0;box-sizing:border-box}
html,body{width:1200px;height:3429px;overflow:hidden}
body{position:relative;background:var(--white);font-family:'Roboto',Arial,sans-serif;color:var(--ink)}
.abs{position:absolute}
svg{display:block}

/* Hero */
.hero{left:0;top:0;width:1200px;height:690px}
.hero-photo{position:absolute;inset:0;background:linear-gradient(115deg,#0d1116 0%,#2a2f36 38%,#5a6068 60%,#2b3036 78%,#101317 100%)}
.hero-curve{position:absolute;left:0;bottom:0}
.logo{left:100px;top:34px;display:flex;align-items:center;gap:12px;color:var(--white);font-size:30px;font-weight:700;letter-spacing:1px}
.logo-mark{width:30px;height:30px;background:var(--white)}
.call{left:860px;top:28px;display:flex;align-items:center;gap:12px;color:var(--white);font-size:17px}
.call-ico{width:40px;height:40px;border:2px solid var(--white);border-radius:50%;display:flex;align-items:center;justify-content:center}
.nav{left:458px;top:92px;display:flex;gap:0;color:var(--white);font-size:17px;font-weight:500}
.nav a{color:inherit;text-decoration:none;margin-right:44px}
.sign-in{left:997px;top:86px;width:104px;height:34px;border-radius:17px;background:var(--blue);color:var(--white);font-size:13px;font-weight:700;display:flex;align-items:center;justify-content:center;gap:6px}
.hero-title{left:0;width:1200px;top:280px;text-align:center;color:var(--white);font-size:94px;font-weight:900;letter-spacing:1px}
.hero-sub{left:0;width:1200px;top:394px;text-align:center;color:var(--white);font-size:17px}
.scan{left:233px;top:448px;width:735px;height:86px;background:rgba(255,255,255,.82);display:flex;align-items:center;padding:0 18px;gap:6px}
.scan .field{width:172px;height:38px;background:var(--white);font-size:13px;font-style:italic;color:#9a9a9a;padding:11px 14px}
.scan .btn{width:172px;height:38px;background:var(--blue-dark);color:var(--white);font-weight:700;font-size:14px;display:flex;align-items:center;justify-content:center}
.arrow-c{width:44px;height:44px;border-radius:50%;background:rgba(255,255,255,.25);display:flex;align-items:center;justify-content:center}
.dots{left:563px;top:630px;display:flex;gap:5px}
.dots span{width:11px;height:11px;border-radius:50%;border:1.5px solid var(--white)}
.dots span.on{background:var(--white)}

/* Shared */
.sec-title{left:0;width:1200px;text-align:center;font-size:35px;font-weight:500;color:var(--ink)}
.ghost{font-size:50px;font-weight:700;color:var(--ghost);writing-mode:vertical-rl;transform:rotate(180deg);letter-spacing:2px}
.btn-o{height:40px;border:2px solid var(--blue);border-radius:20px;color:var(--blue);font-size:14px;font-weight:700;display:flex;align-items:center;justify-content:center}

/* Services */
.service{width:330px;text-align:center}
.service .icon{height:60px;display:flex;justify-content:center;align-items:flex-end}
.service h3{margin-top:12px;font-size:16px;font-weight:500}
.service p{margin-top:14px;font-size:12.5px;line-height:25px;color:var(--muted)}
.v-rule{width:1px;height:170px;background:var(--line)}

/* About */
.about-bg{left:0;top:1180px;width:1200px;height:670px}
.about-photo{position:absolute;inset:0;background:linear-gradient(100deg,#b9bcc1 0%,#d7d9dc 35%,#c7c9cc 60%,#bdbfc2 100%)}
.about-veil{position:absolute;inset:0;background:rgba(255,255,255,.55)}
.about-text{left:200px;top:1432px;width:800px;text-align:center;font-size:12.5px;line-height:34px;color:#555}
.btn-fill{height:44px;border-radius:22px;background:var(--blue-dark);color:var(--white);font-size:14px;font-weight:700;display:flex;align-items:center;justify-content:center}

/* News */
.news-card{top:1975px;width:318px;height:192px;border:1px solid #cfcfcf;border-left:5px solid var(--blue);background:var(--white);padding:30px 30px}
.news-card.featured{background:var(--grey-card);color:var(--white)}
.news-card .date{font-size:12px;color:var(--blue)}
.news-card.featured .date{color:var(--white)}
.news-card h4{margin-top:20px;font-size:15px;font-weight:500;line-height:25px}
.news-card p{margin-top:10px;font-size:12px;line-height:22px;color:var(--muted)}
.news-card.featured p{color:#e6e6e6}

/* Testimonials */
.testi{left:0;top:2290px;width:1200px;height:540px}
.portrait{left:161px;top:2468px;width:176px;height:176px;border-radius:50%;border:5px solid var(--white);background:radial-gradient(circle at 50% 40%,#8a7665 0%,#4b4038 55%,#2a2522 100%)}
.quote{left:366px;top:2478px;width:690px;color:var(--white);font-size:13px;font-style:italic;line-height:30px}
.quote-name{left:366px;top:2612px;color:var(--white);font-size:16px;font-weight:700;letter-spacing:.5px}

/* Contact */
.input{left:135px;width:450px;height:44px;border:1px solid var(--line);display:flex;align-items:center;justify-content:space-between;padding:0 16px;font-size:13px;color:#9a9a9a}
.textarea{left:613px;top:2935px;width:453px;height:173px;border:1px solid var(--line);padding:14px 16px;font-size:13px;color:#9a9a9a}
.send{left:521px;top:3155px;width:160px;height:42px;border:2px solid var(--blue);border-radius:4px;color:var(--blue);font-size:15px;font-weight:700;display:flex;align-items:center;justify-content:center}
.contact-row{left:216px;top:3232px;display:flex;align-items:center;font-size:13px;color:#333}
.ring{width:46px;height:46px;border-radius:50%;border:1.5px solid #bbb;display:flex;align-items:center;justify-content:center}
.social{display:flex;gap:8px;margin-left:22px}
.social .ring{border-color:#999}
.social .sq{width:12px;height:12px;background:#333}

/* Footer */
.footer{left:0;top:3360px;width:1200px;height:69px;background:var(--footer);color:#ddd;font-size:12px}
.footer .copy{position:absolute;left:100px;top:28px}
.footer .links{position:absolute;right:104px;top:28px;display:flex;gap:10px}
</style>
</head>
<body>

<!-- Hero -->
<section class="abs hero">
  <div class="hero-photo" role="img" aria-label="Dark workspace photo of a person typing on a laptop"></div>
  <svg class="hero-curve" width="1200" height="70" viewBox="0 0 1200 70"><path d="M0 70 L0 20 Q600 -25 1200 20 L1200 70 Z" fill="#fff"/></svg>
</section>

<div class="abs logo"><span class="logo-mark"></span>Kovel Digital</div>
<div class="abs call">
  <span class="call-ico"><svg width="18" height="18" viewBox="0 0 24 24"><path d="M6.6 10.8a15 15 0 0 0 6.6 6.6l2.2-2.2c.3-.3.7-.4 1-.2 1.1.4 2.3.6 3.6.6.6 0 1 .4 1 1V20c0 .6-.4 1-1 1A17 17 0 0 1 3 4c0-.6.4-1 1-1h3.5c.6 0 1 .4 1 1 0 1.3.2 2.5.6 3.6.1.3 0 .7-.2 1z" fill="#fff"/></svg></span>
  Call Us : 1 800 555 0142
</div>
<nav class="abs nav"><a>Home</a><a>About us</a><a>What we do</a><a>News</a><a>Contact Us</a></nav>
<div class="abs sign-in"><svg width="11" height="11" viewBox="0 0 24 24"><circle cx="12" cy="7" r="5" fill="#fff"/><path d="M2 23c0-6 4.5-9 10-9s10 3 10 9z" fill="#fff"/></svg>SIGN IN</div>

<h1 class="abs hero-title">KOVEL DIGITAL</h1>
<p class="abs hero-sub">We supply digital marketing services to those companies who demand a strong return on investment</p>
<div class="abs scan">
  <div class="field">http://</div><div class="field">Keyword</div><div class="field">Email</div><div class="btn">SCAN NOW !</div>
</div>
<div class="abs arrow-c" style="left:44px;top:394px"><svg width="14" height="14" viewBox="0 0 14 14"><path d="M9 2 4 7l5 5" stroke="#fff" stroke-width="2" fill="none"/></svg></div>
<div class="abs arrow-c" style="left:1110px;top:394px"><svg width="14" height="14" viewBox="0 0 14 14"><path d="M5 2l5 5-5 5" stroke="#fff" stroke-width="2" fill="none"/></svg></div>
<div class="abs dots"><span class="on"></span><span></span><span></span><span></span><span></span></div>

<!-- Services -->
<h2 class="abs sec-title" style="top:773px">OUR SERVICES</h2>
<div class="abs ghost" style="left:1108px;top:720px">OUR SERVICES</div>

<div class="abs service" style="left:89px;top:880px">
  <div class="icon"><svg width="56" height="56" viewBox="0 0 56 56"><circle cx="23" cy="23" r="15" stroke="var(--blue)" stroke-width="6" fill="none"/><path d="M34 34l16 16" stroke="var(--blue)" stroke-width="8" stroke-linecap="round"/></svg></div>
  <h3>SEO</h3>
  <p>Excepteur sint occaecat cupidatat non proident,<br>sunt in culpa qui officia deserunt mollit anim id<br>est lasantium doloremqborum velit esse cill.</p>
</div>
<div class="abs v-rule" style="left:430px;top:900px"></div>
<div class="abs service" style="left:434px;top:880px">
  <div class="icon"><svg width="62" height="54" viewBox="0 0 62 54"><rect x="2" y="2" width="58" height="38" rx="3" fill="var(--blue)"/><rect x="7" y="7" width="48" height="28" fill="#fff"/><rect x="25" y="40" width="12" height="8" fill="var(--blue)"/><rect x="17" y="47" width="28" height="5" rx="2" fill="var(--blue)"/></svg></div>
  <h3>WEBSITE DEVELOPMENT</h3>
  <p>Excepteur sint occaecat cupidatat non proident,<br>sunt in culpa qui officia deserunt mollit anim id<br>est lasantium doloremqborum velit esse cill.</p>
</div>
<div class="abs v-rule" style="left:777px;top:900px"></div>
<div class="abs service" style="left:779px;top:876px">
  <div class="icon"><svg width="46" height="56" viewBox="0 0 46 56"><circle cx="23" cy="14" r="12" fill="var(--blue)"/><path d="M2 56c0-17 9-27 21-27s21 10 21 27z" fill="var(--blue)"/></svg></div>
  <h3>LEAD GENERATION</h3>
  <p>Excepteur sint occaecat cupidatat non proident,<br>sunt in culpa qui officia deserunt mollit anim id<br>est lasantium doloremqborum velit esse cill.</p>
</div>
<div class="abs btn-o" style="left:514px;top:1110px;width:172px">VIEW ALL SERVICES</div>

<!-- About -->
<section class="abs about-bg">
  <div class="about-photo" role="img" aria-label="Faded photo of hands using a tablet with digital marketing icons overlay"></div>
  <div class="about-veil"></div>
  <svg class="abs" style="left:0;top:0" width="1200" height="80" viewBox="0 0 1200 80"><path d="M0 0 H1200 V10 Q700 110 0 10 Z" fill="#fff"/><path d="M0 -4 Q260 30 560 64 Q280 40 0 14 Z" fill="var(--navy)"/></svg>
  <svg class="abs" style="left:0;bottom:0" width="1200" height="80" viewBox="0 0 1200 80"><path d="M0 80 V55 Q500 -10 1200 60 V80 Z" fill="#fff"/><path d="M800 10 Q1000 22 1200 60 L1200 72 Q1010 30 800 10 Z" fill="var(--blue)"/></svg>
</section>
<h2 class="abs sec-title" style="top:1368px">ABOUT US</h2>
<div class="abs ghost" style="left:1108px;top:1355px;color:rgba(255,255,255,.6)">ABOUT US</div>
<p class="abs about-text">Sed ut perspiciatis unde omnis iste natus error sit voluptatem accusantium doloremque laudantium, totam rem aperiam, eaque ipsa quae ab illo inventore veritatis et quasi architecto beatae vitae dicta sunt explicabo. Nemo enim ipsam voluptatem quia voluptas sit aspernatur aut odit aut fugit, sed quia consequuntur magni dolores eos qui ratione voluptatem sequi nesciunt. Neque porro quisquam est, qui dolorem ipsum quia dolor sit amet, consectetur adipisci velit, sed quia non numquam eius modi tempora incidunt ut labore et dolore magnam aliquam quaerat</p>
<div class="abs btn-fill" style="left:516px;top:1601px;width:168px">READ MORE INFO</div>

<!-- News -->
<h2 class="abs sec-title" style="top:1882px">LATEST NEWS</h2>
<div class="abs ghost" style="left:1122px;top:1890px">NEWS</div>
<svg class="abs" style="left:32px;top:2050px" width="24" height="44" viewBox="0 0 24 44"><path d="M20 2 4 22l16 20" stroke="#777" stroke-width="2" fill="none"/></svg>
<svg class="abs" style="left:1136px;top:2050px" width="24" height="44" viewBox="0 0 24 44"><path d="M4 2l16 20-16 20" stroke="#777" stroke-width="2" fill="none"/></svg>
<article class="abs news-card" style="left:96px"><div class="date">Aug 20,2018</div><h4>SED UT PERSPICIATIS UNDE<br>OMNIS ISTE NATU</h4><p>Neque porro quisquam est, qui dolorem ipsum<br>quiaame consectetur adipisci .</p></article>
<article class="abs news-card featured" style="left:437px"><div class="date">Aug 20,2018</div><h4>SED UT PERSPICIATIS UNDE<br>OMNIS ISTE NATU</h4><p>Neque porro quisquam est, qui dolorem ipsum<br>quiaame consectetur adipisci .</p></article>
<article class="abs news-card" style="left:777px"><div class="date">Aug 20,2018</div><h4>SED UT PERSPICIATIS UNDE<br>OMNIS ISTE NATU</h4><p>Neque porro quisquam est, qui dolorem ipsum<br>quiaame consectetur adipisci .</p></article>
<div class="abs btn-o" style="left:519px;top:2220px;width:153px">VIEW ALL NEWS</div>

<!-- Testimonials -->
<svg class="abs testi" width="1200" height="540" viewBox="0 0 1200 540">
  <path d="M0 4 Q300 30 600 52 Q300 24 0 14 Z" fill="var(--navy)"/>
  <path d="M0 70 Q600 -10 1200 30 V480 Q600 400 0 520 Z" fill="var(--blue)"/>
  <path d="M900 430 Q1080 450 1200 480 L1200 470 Q1080 440 900 430 Z" fill="var(--navy)"/>
</svg>
<div class="abs ghost" style="left:1118px;top:2380px;color:rgba(255,255,255,.16)">TESTIMONIALS</div>
<svg class="abs" style="left:100px;top:2535px" width="22" height="44" viewBox="0 0 22 44"><path d="M18 2 4 22l14 20" stroke="#fff" stroke-width="2" fill="none"/></svg>
<svg class="abs" style="left:1078px;top:2535px" width="22" height="44" viewBox="0 0 22 44"><path d="M4 2l14 20-14 20" stroke="#fff" stroke-width="2" fill="none"/></svg>
<div class="abs portrait" role="img" aria-label="Circular portrait photo of the client giving the testimonial"></div>
<p class="abs quote">" Sed ut perspiciatis unde omnis iste natus error sit voluptatem accusantium doloremque laudantium, totam rem aperiam, eaque ipsa quae ab illo inventore veritatis et quasi architecto beatae vitae dicta sunt explicabo. Nemo enim ipsam voluptatem quia voluptas sit aspernatur aut odit aut fugit, sed quia consequuntur magni dolores eos qui ratione voluptatem sequi nesciunt. Neque porro quisquam est, qui dolorem ipsum quia dolor sit amet "</p>
<div class="abs quote-name">- ADIPISCI VELIT</div>
<svg class="abs" style="left:872px;top:2628px" width="124" height="76" viewBox="0 0 124 76"><g fill="rgba(255,255,255,.3)"><circle cx="30" cy="46" r="28"/><path d="M4 46 Q8 8 44 0 Q22 16 22 40z"/><circle cx="92" cy="46" r="28"/><path d="M66 46 Q70 8 106 0 Q84 16 84 40z"/></g></svg>

<!-- Contact -->
<h2 class="abs sec-title" style="top:2845px">CONTACT FORM</h2>
<div class="abs ghost" style="left:1115px;top:2935px">CONTACT US</div>
<div class="abs input" style="top:2935px">First &amp; Last name<svg width="20" height="20" viewBox="0 0 24 24"><circle cx="12" cy="7" r="5" fill="#aaa"/><path d="M2 23c0-6 4.5-9 10-9s10 3 10 9z" fill="#aaa"/></svg></div>
<div class="abs input" style="top:2999px">Phone No.<svg width="18" height="18" viewBox="0 0 24 24"><path d="M6.6 10.8a15 15 0 0 0 6.6 6.6l2.2-2.2c.3-.3.7-.4 1-.2 1.1.4 2.3.6 3.6.6.6 0 1 .4 1 1V20c0 .6-.4 1-1 1A17 17 0 0 1 3 4c0-.6.4-1 1-1h3.5c.6 0 1 .4 1 1 0 1.3.2 2.5.6 3.6.1.3 0 .7-.2 1z" fill="#aaa"/></svg></div>
<div class="abs input" style="top:3063px">Email Id *<svg width="20" height="16" viewBox="0 0 20 16"><rect x="1" y="1" width="18" height="14" fill="none" stroke="#aaa" stroke-width="1.5"/><path d="M1 1l9 8 9-8" fill="none" stroke="#aaa" stroke-width="1.5"/></svg></div>
<div class="abs textarea">your message</div>
<div class="abs send">Send Message</div>

<div class="abs contact-row">
  <span class="ring"><svg width="14" height="20" viewBox="0 0 14 20"><rect x="1" y="1" width="12" height="18" rx="2" fill="none" stroke="#333" stroke-width="1.6"/><circle cx="7" cy="15.5" r="1.2" fill="#333"/></svg></span>
  <span style="margin-left:18px">Tap-To-Call: (800) 555 0142</span>
  <span class="ring" style="margin-left:30px"><svg width="18" height="14" viewBox="0 0 20 16"><rect x="1" y="1" width="18" height="14" fill="none" stroke="#333" stroke-width="1.6"/><path d="M1 1l9 8 9-8" fill="none" stroke="#333" stroke-width="1.6"/></svg></span>
  <span style="margin-left:18px">Email &nbsp;: &nbsp;hello@koveldigital-studio.net</span>
  <div class="social"><span class="ring"><span class="sq"></span></span><span class="ring"><span class="sq"></span></span><span class="ring"><span class="sq"></span></span><span class="ring"><span class="sq"></span></span></div>
</div>

<footer class="abs footer">
  <div class="copy">© copyright 2018 Kovel Digital.All Rights Reserved</div>
  <div class="links"><span>Privacy Policy</span><span>|</span><span>Terms and Use</span><span>|</span><span>Sitemap</span></div>
</footer>

</body>
</html>
```